Corrugated Boxes and Digitally Printed Promo Display Brochure

We need a brochure design for our company product offerings and capabilities, based in Dorrington, MA called Brindle-Crest, Inc. We make corrugated boxes and displays for B2B, using innovative machinery, in a 100% solar powered facility making us one of the most sustainable manufacturer's in New England. Our main product is "corrugated brown boxes," primarily used for shipping, high volume, and low cost (competitive pricing). Our next main product is "standard displays," primarily used for promotional purposes for various industries, using digital printing and high graphic flexo. And lastly, our third category of product is "retail packaging and eCommerce," primarily used for promotional packaging using digital and high graphic flexo inside / outside the box. Our competitive advantage is that we have three key things: 2 corrugators (high volume, low cost), sustainability (energy efficiency), and warehousing & fulfillment (storage & assembly). We would like to see designs that use our company colors; red, orange, yellow. You may used black or grey accents, if appropriate. The final design should communicate our ability to make high quality corrugated boxes and displays at competitive pricing, thanks to our advanced machinery and 100% solar powered plant, thereby making us the most sustainable corrugated box provider in New England. We want the design to be clean and professional, nothing too busy. We want room for pictures and short bullet text.
Important to note: our trucks have a tagline saying "Sustainable packaging for a greener, cleaner, better tomorrow."
Updates
Looking for only trifold brochure designs. Thank you.
Looking for additional trifold designs. We would like a QR code linking back to our website included on the "back" panel of the brochure with our contact information. We would also like more room for photos and less words (we plan on doing short bullet points for each product category -- corrugated packaging, standard displays, and retail packaging & eCommerce). One page dedicated to our sustainability i.e. "the most sustainable packaging provider in New England" with a picture of our solar panels or stock solar panels and maybe a solar seal symbol somewhere. Front cover should have a mixture of our product offerings; couple displays, a couple boxes, and some eCommerce to advertise everything we make and do.

```html
<!DOCTYPE html>
<html lang="en">
<head>
<meta charset="utf-8">
<title>Brindle-Crest Trifold Brochure</title>
<link href="https://fonts.googleapis.com/css2?family=Mulish:wght@400;600;700;800&display=swap" rel="stylesheet">
<style>
  :root{
    --backdrop:#58585a;
    --red:#e8262a;
    --orange:#f28c1f;
    --yellow:#f5c21a;
    --white:#ffffff;
    --ink:#231f20;
    --rule:#c9c9c9;
    --kraft-light:#e6b877;
    --kraft-dark:#b9803e;
  }
  *{box-sizing:border-box;margin:0;padding:0}
  html,body{width:1200px;height:549px;overflow:hidden}
  body{background:var(--backdrop);font-family:"Mulish",sans-serif;position:relative}
  .brochure{position:absolute;left:53px;top:80px;width:1094px;height:389px;background:var(--white);box-shadow:2px 4px 6px rgba(0,0,0,.35);overflow:hidden}
  .block{position:absolute}
  .red-panel{left:0;top:0;width:414px;height:140px;background:var(--red)}
  .logo-tab{left:414px;top:0;width:111px;height:170px;background:var(--orange);z-index:3}
  .contact-panel{left:0;top:147px;width:275px;height:137px;background:var(--orange)}
  .about-panel{left:548px;top:0;width:396px;height:164px;background:var(--red)}
  .feature-panel{left:640px;top:164px;width:304px;height:127px;background:var(--orange)}
  .photo{position:absolute}
  .photo-boxes{left:275px;top:147px;width:274px;height:137px;background:linear-gradient(160deg,var(--kraft-light),var(--kraft-dark) 70%,#8a5a2a)}
  .photo-rolls{left:944px;top:0;width:135px;height:282px;background:linear-gradient(90deg,#b8ab98,#d9c8ad 40%,#c4a47a 70%,#a88a62)}
  .photo-solar{left:548px;top:178px;width:132px;height:189px;background:linear-gradient(135deg,#d9d9de,#3d3f48 45%,#e4e4ea 60%,#2c2e36);z-index:2}
  .heading{color:var(--white);font-weight:700;font-size:6.6px;letter-spacing:.1px;text-transform:uppercase;line-height:8.4px}
  .body{color:var(--white);font-weight:600;font-size:4.5px;line-height:7.8px;text-transform:uppercase;text-align:justify}
  .body p+p{margin-top:7.8px}
  .strengths{position:absolute;left:19px;top:19px}
  .strengths ul{list-style:none;margin-top:3px}
  .strengths li{color:var(--white);font-weight:600;font-size:4.5px;line-height:7.8px;text-transform:uppercase}
  .contact{position:absolute;left:20px;top:170px;color:var(--white)}
  .contact h2{font-size:8px;font-weight:800;margin-bottom:10px}
  .contact-row{display:flex;align-items:center;gap:27px;height:22px}
  .contact-icon{width:16px;height:16px;border-radius:50%;background:var(--white);display:flex;align-items:center;justify-content:center}
  .contact-text{font-size:6px;font-weight:600;line-height:9px}
  .wordmark{font-weight:700;letter-spacing:.3px;display:flex;align-items:center;gap:4px}
  .wordmark-mark{width:9px;height:9px}
  .logo-tab .wordmark{position:absolute;left:9px;top:141px;color:var(--white);font-size:8.5px}
  .logo-tab .wordmark-mark{background:var(--white)}
  .footer-wordmark{position:absolute;left:19px;top:302px;color:var(--red);font-size:10px}
  .footer-wordmark .wordmark-mark{width:11px;height:11px;background:var(--orange)}
  .tagline{position:absolute;left:286px;top:299px;width:203px}
  .tagline h1{color:var(--red);font-size:13px;font-weight:800;line-height:15px;white-space:nowrap}
  .tagline p{color:var(--orange);font-size:8.2px;font-weight:700;line-height:10px;margin-top:3px;white-space:nowrap}
  .tagline .underline{height:1px;background:var(--rule);margin-top:3px;position:relative}
  .tagline .underline::before{content:"";position:absolute;left:0;top:0;width:86px;height:1px;background:var(--red)}
  .solar-seal{position:absolute;left:237px;top:359px;width:15px;height:15px;border-radius:50%;background:var(--yellow);border:1.5px solid #e0a812}
  .about{position:absolute;left:563px;top:16px;width:248px}
  .ecommerce{position:absolute;left:832px;top:16px;width:106px}
  .protective{position:absolute;left:696px;top:177px;width:107px}
  .commitment{position:absolute;left:838px;top:177px;width:100px}
  .about .heading,.ecommerce .heading{margin-bottom:10px}
  .protective .heading,.commitment .heading{margin-bottom:5px}
  .product-thumb{position:absolute;top:296px;width:41px;height:29px;background:var(--red);display:flex;align-items:center;justify-content:center}
  .product-thumb span{display:block;width:22px;height:15px;background:linear-gradient(160deg,var(--kraft-light),var(--kraft-dark))}
  .thumb-boxes{left:725px}
  .thumb-displays{left:863px}
  .thumb-retail{left:995px}
  .product{position:absolute;top:332px}
  .product h3{color:var(--ink);font-size:6.2px;font-weight:700;text-transform:uppercase;margin-bottom:6px;white-space:nowrap}
  .product p{color:var(--ink);font-size:4.5px;font-weight:700;line-height:7.8px;text-transform:uppercase;text-align:justify}
  .product-boxes{left:696px;width:92px}
  .product-displays{left:832px;width:102px}
  .product-retail{left:953px;top:335px;width:121px}
</style>
</head>
<body>
<main class="brochure">
  <div class="block red-panel">
    <section class="strengths">
      <h2 class="heading">Corrugators</h2>
      <ul>
        <li>High volume, low cost.</li>
        <li>Sustainability (energy efficiency),</li>
        <li>Warehousing &amp; fulfillment (storage &amp; assembly)</li>
      </ul>
    </section>
  </div>

  <div class="block contact-panel"></div>
  <section class="contact">
    <h2>CONTACT US :</h2>
    <div class="contact-row">
      <div class="contact-icon"><svg width="9" height="9" viewBox="0 0 24 24"><path fill="#f28c1f" d="M6.6 10.8a15 15 0 0 0 6.6 6.6l2.2-2.2a1 1 0 0 1 1-.25 11.4 11.4 0 0 0 3.6.57 1 1 0 0 1 1 1V20a1 1 0 0 1-1 1A17 17 0 0 1 3 4a1 1 0 0 1 1-1h3.5a1 1 0 0 1 1 1c0 1.25.2 2.45.57 3.57a1 1 0 0 1-.25 1z"/></svg></div>
      <div class="contact-text">+000 123 456 789<br>+000 123 456 789</div>
    </div>
    <div class="contact-row">
      <div class="contact-icon"><svg width="9" height="9" viewBox="0 0 24 24"><path fill="#f28c1f" d="M3 5h18v14H3z"/><path fill="none" stroke="#fff" stroke-width="2" d="M3 5l9 8 9-8"/></svg></div>
      <div class="contact-text">yourgmail@name.com<br>www.websitename.com</div>
    </div>
    <div class="contact-row">
      <div class="contact-icon"><svg width="9" height="9" viewBox="0 0 24 24"><path fill="#f28c1f" d="M12 2a7 7 0 0 0-7 7c0 5 7 13 7 13s7-8 7-13a7 7 0 0 0-7-7zm0 9.5A2.5 2.5 0 1 1 12 6.5a2.5 2.5 0 0 1 0 5z"/></svg></div>
      <div class="contact-text">Your Street Address Here<br>New Yerk City, Zip - 000</div>
    </div>
  </section>

  <div class="photo photo-boxes" role="img" aria-label="Stacked corrugated shipping boxes with a delivery receipt clipboard"></div>

  <div class="block logo-tab">
    <div class="wordmark"><span class="wordmark-mark"></span>BRINDLE-CREST</div>
  </div>

  <div class="wordmark footer-wordmark"><span class="wordmark-mark"></span>BRINDLE-CREST</div>

  <section class="tagline">
    <h1>SUSTAINABLE PACKAGING</h1>
    <p>FOR A GREENER, CLEANER, BETTER TOMORROW</p>
    <div class="underline"></div>
  </section>

  <div class="solar-seal" role="img" aria-label="Solar seal"></div>

  <div class="block about-panel"></div>
  <section class="about">
    <h2 class="heading">About the company</h2>
    <div class="body">
      <p>Brindle-Crest Packaging is a third generation family business, owned and operated by Dean Brindle, Marc Harlow, and Lena Moretti. It was founded as Brindle Box Co. in 1941 by Brindle's grandfather, Elliot, and great uncle, Frank. It was passed down to the second generation, Victor and Hugh Brindle, who successfully operated the company for many years, investing in flexo and litho printing innovations.</p>
      <p>Around the same time, Crest Container was transitioning from Walter Harlow to second generation leadership that included Marc and Lena. They had the vision and foresight to secure a guaranteed source of sheets by investing in Corrvale Packaging, a sheetfeeder co-op. In 2004, the merger of Brindle Box and Crest Container resulted in Brindle-Crest Packaging, now located in Dorrington, MA.</p>
      <p>Through the acquisitions of Minuteman Packaging, Boxworks Unlimited, and most recently Laurent Packaging, a protective packaging division was formed, offering both foam and wood crating products. The facility is located in Millbrook, MA.</p>
    </div>
  </section>

  <section class="ecommerce">
    <h2 class="heading">E-commerce solutions</h2>
    <div class="body">
      <p>With 58 billion packages delivered each year, e-commerce companies face unique packaging challenges. You must be durable enough to survive shipping, dazzling enough to deliver a memorable unboxing experience, and streamlined enough to be environmentally friendly.</p>
      <p>Brindle-Crest Packaging offers complete design services from prototype to finished product to help you boost your brand recognition while reducing your carbon footprint. We offer the most advanced digital printing.</p>
    </div>
  </section>

  <div class="photo photo-rolls" role="img" aria-label="Large rolls of kraft paper stacked in a warehouse"></div>

  <div class="block feature-panel"></div>
  <div class="photo photo-solar" role="img" aria-label="Aerial view of solar panel arrays on the factory roof"></div>

  <section class="protective">
    <h2 class="heading">Protective packaging</h2>
    <div class="body">
      <p>For products that range from small, sensitive, scientific instrumentation to oversized equipment for aerospace and defense systems, the protective packaging group at Brindle-Crest packaging provides the most effective and efficient packaging and crating solutions to support today's wide array of industries. In addition to seeing your goods have been packaged to arrive safely, we help streamline your supply chain and delivery process to help minimize costs.</p>
    </div>
  </section>

  <section class="commitment">
    <h2 class="heading">Our commitment to sustainability and the future of our planet.</h2>
    <div class="body">
      <p>When Brindle-Crest relocated its manufacturing facility in 2016 from Millbrook, MA to Dorrington, MA – a facility built in the late 1970's – we understood renovations would be necessary. However, from planning through production, we were insistent that a keen focus be kept on sustainability.</p>
    </div>
  </section>

  <div class="product-thumb thumb-boxes" role="img" aria-label="Open corrugated brown box"><span></span></div>
  <div class="product-thumb thumb-displays" role="img" aria-label="Standard display tray"><span></span></div>
  <div class="product-thumb thumb-retail" role="img" aria-label="Printed retail product packaging"><span></span></div>

  <section class="product product-boxes">
    <h3>Corrugated brown boxes</h3>
    <p>Primarily used for shipping, high volume, and low cost (competitive pricing).</p>
  </section>
  <section class="product product-displays">
    <h3>Standard displays</h3>
    <p>Primarily used for promotional purposes for various industries, using digital printing and high graphic flexo.</p>
  </section>
  <section class="product product-retail">
    <h3>Retail packaging and ecommerce</h3>
    <p>Primarily used for promotional packaging using digital and high graphic flexo inside / outside the box</p>
  </section>
</main>
</body>
</html>
```